Clear plastic business card for window cleaning company

hi guys
i run a window cleaning company and need a new business card design. i want a design for a clear or frosted plastic business card.
i have uploaded my logo and a silhouette of a guy abseiling
thought maybe the clear card could simulate a clear window or windows.
the abseiler doesn't have to be used but i think it looks good if it could be incorporated into the design as we clean all windows from houses to high rise buildings

my name is dean marlow
phone number is 0438 602 917
email dean@glazoria.net.au
web www.glazoria.net.au
services offered are
window cleaning
high pressure cleaning
building washdowns
gutter cleaning
difficult access specialist
abseiling
elevated work platforms
commercial/domestic/high-rise

Contact Information for Business Card

my name is dean marlow
email dean@glazoria.net.au
web www.glazoria.net.au
services offered are
window cleaning
high pressure cleaning
building washdowns
gutter cleaning
abseiling
elevated work platforms

Requirements
Must have
• cool design that stands out i want the clear or frosted card to simulate a window to get a stand out effect

```html
<!DOCTYPE html>
<html lang="en">
<head>
<meta charset="utf-8">
<title>Glazoria Services – Clear Business Card</title>
<link rel="stylesheet" href="https://fonts.googleapis.com/css2?family=Roboto+Condensed:wght@400;700;800&family=Roboto:wght@400;500&display=swap">
<style>
  :root {
    --page: #e9edf1;
    --blue: #1f6fb8;
    --blue-deep: #0e4f93;
    --blue-glass: rgba(31, 111, 184, 0.78);
    --blue-glass-light: rgba(120, 178, 226, 0.55);
    --green: #7cc242;
    --ink: #16324f;
    --white: #ffffff;
    --frost: rgba(255, 255, 255, 0.72);
    --edge: rgba(255, 255, 255, 0.9);
  }
  * { box-sizing: border-box; margin: 0; padding: 0; }
  html, body {
    width: 814px; height: 1200px; overflow: hidden;
    background: var(--page);
    font-family: "Roboto", sans-serif;
  }
  .canvas {
    position: relative; width: 814px; height: 1200px;
    display: flex; flex-direction: column; align-items: center;
    justify-content: center; gap: 90px;
  }
  .card {
    position: relative; width: 640px; height: 366px;
    border-radius: 8px; overflow: hidden;
    border: 1px solid var(--edge);
    box-shadow: 0 10px 30px rgba(22, 50, 79, 0.18);
  }

  /* ---------- front ---------- */
  .card--front {
    background: linear-gradient(180deg, rgba(200, 222, 240, 0.6) 0%, rgba(160, 200, 232, 0.7) 100%);
  }
  .front-header {
    position: absolute; left: 0; top: 0; width: 100%; height: 150px;
    background: linear-gradient(90deg, var(--frost) 0%, rgba(255,255,255,0.45) 60%, rgba(180,212,238,0.5) 100%);
  }
  .handle-line {
    position: absolute; left: 16px; top: 0; width: 4px; height: 100%;
    background: rgba(255,255,255,0.85);
  }
  .brand {
    position: absolute; left: 58px; top: 30px;
    display: flex; align-items: center; gap: 12px;
  }
  .brand-mark {
    width: 34px; height: 34px; background: var(--blue);
  }
  .brand-name {
    font-family: "Roboto Condensed", sans-serif; font-weight: 800;
    font-size: 34px; line-height: 1; color: var(--blue-deep);
    text-transform: uppercase; letter-spacing: 0.5px;
  }
  .brand-line {
    position: absolute; left: 104px; top: 72px;
    font-family: "Roboto Condensed", sans-serif; font-weight: 800;
    font-size: 20px; color: var(--blue-deep);
  }
  .front-body {
    position: absolute; left: 0; top: 150px; width: 100%; height: 216px;
    background: linear-gradient(180deg, var(--blue-glass) 0%, var(--blue-glass-light) 100%);
  }
  .name-bar {
    position: absolute; right: 0; top: 128px; width: 330px; height: 34px;
    background: var(--green);
    display: flex; align-items: center; justify-content: flex-end; padding-right: 22px;
    font-family: "Roboto Condensed", sans-serif; font-weight: 700;
    font-size: 22px; color: var(--ink); text-transform: uppercase; letter-spacing: 0.5px;
  }
  .contact-list {
    position: absolute; left: 58px; top: 196px; list-style: none;
    display: flex; flex-direction: column; gap: 10px;
  }
  .contact-list li {
    display: flex; align-items: center; gap: 10px;
    font-size: 15px; color: var(--white);
  }
  .contact-list svg { width: 16px; height: 16px; flex: none; }

  /* ---------- back ---------- */
  .card--back {
    background: linear-gradient(180deg, rgba(255,255,255,0.6) 0%, rgba(225,236,245,0.55) 100%);
  }
  .back-line {
    position: absolute; left: 0; top: 50px; width: 6px; height: 236px;
    background: var(--blue);
  }
  .service-list {
    position: absolute; left: 26px; top: 92px; list-style: none;
    display: flex; flex-direction: column; gap: 4px;
  }
  .service-list li {
    display: flex; align-items: center; gap: 8px;
    font-family: "Roboto Condensed", sans-serif; font-weight: 700;
    font-size: 17px; line-height: 1.2; color: var(--blue-deep);
  }
  .service-list svg { width: 13px; height: 13px; flex: none; }
  .rope {
    position: absolute; left: 500px; top: 0; width: 2px; height: 190px;
    background: var(--blue-deep);
  }
  .abseiler {
    position: absolute; left: 440px; top: 180px; width: 130px; height: 130px;
    border-radius: 40% 50% 45% 50%;
    background: radial-gradient(circle at 50% 45%, rgba(14,79,147,0.85), rgba(14,79,147,0.35) 70%, rgba(14,79,147,0) 100%);
  }
</style>
</head>
<body>
<main class="canvas">

  <section class="card card--front" aria-label="Business card front">
    <div class="front-header"></div>
    <div class="front-body"></div>
    <div class="handle-line"></div>

    <div class="brand">
      <span class="brand-mark"></span>
      <span class="brand-name">Glazoria Services</span>
    </div>
    <div class="brand-line">1300 452 946</div>

    <div class="name-bar">Dean Marlow</div>

    <ul class="contact-list">
      <li>
        <svg viewBox="0 0 16 16" aria-hidden="true"><path fill="#fff" d="M3.6 1.5l2.3 2.4-1.2 1.8c.9 1.9 2.4 3.4 4.3 4.3l1.8-1.2 2.4 2.3-1.4 2.4C6.9 13.2 2.8 9.1 2.4 3.2z"/></svg>
        0438 602 917
      </li>
      <li>
        <svg viewBox="0 0 16 16" aria-hidden="true"><rect x="1.5" y="3.5" width="13" height="9" fill="none" stroke="#fff" stroke-width="1.4"/><path d="M1.5 3.5l6.5 5 6.5-5" fill="none" stroke="#fff" stroke-width="1.4"/></svg>
        dean@glazoria.net.au
      </li>
      <li>
        <svg viewBox="0 0 16 16" aria-hidden="true"><circle cx="8" cy="8" r="6.3" fill="none" stroke="#fff" stroke-width="1.4"/><path d="M1.7 8h12.6M8 1.7c-3 3.5-3 9.1 0 12.6M8 1.7c3 3.5 3 9.1 0 12.6" fill="none" stroke="#fff" stroke-width="1.2"/></svg>
        www.glazoria.net.au
      </li>
    </ul>
  </section>

  <section class="card card--back" aria-label="Business card back">
    <div class="back-line"></div>

    <ul class="service-list">
      <li><svg viewBox="0 0 12 12" aria-hidden="true"><path d="M1.5 6.5l3 3 6-7" fill="none" stroke="#1f6fb8" stroke-width="2"/></svg>window cleaning</li>
      <li><svg viewBox="0 0 12 12" aria-hidden="true"><path d="M1.5 6.5l3 3 6-7" fill="none" stroke="#1f6fb8" stroke-width="2"/></svg>high pressure cleaning</li>
      <li><svg viewBox="0 0 12 12" aria-hidden="true"><path d="M1.5 6.5l3 3 6-7" fill="none" stroke="#1f6fb8" stroke-width="2"/></svg>building washdowns</li>
      <li><svg viewBox="0 0 12 12" aria-hidden="true"><path d="M1.5 6.5l3 3 6-7" fill="none" stroke="#1f6fb8" stroke-width="2"/></svg>gutter cleaning</li>
      <li><svg viewBox="0 0 12 12" aria-hidden="true"><path d="M1.5 6.5l3 3 6-7" fill="none" stroke="#1f6fb8" stroke-width="2"/></svg>difficult access specialist</li>
      <li><svg viewBox="0 0 12 12" aria-hidden="true"><path d="M1.5 6.5l3 3 6-7" fill="none" stroke="#1f6fb8" stroke-width="2"/></svg>abseiling</li>
      <li><svg viewBox="0 0 12 12" aria-hidden="true"><path d="M1.5 6.5l3 3 6-7" fill="none" stroke="#1f6fb8" stroke-width="2"/></svg>elevated work platforms</li>
      <li><svg viewBox="0 0 12 12" aria-hidden="true"><path d="M1.5 6.5l3 3 6-7" fill="none" stroke="#1f6fb8" stroke-width="2"/></svg>commercial/domestic/high-rise</li>
    </ul>

    <div class="rope"></div>
    <div class="abseiler" role="img" aria-label="Blue silhouette of a window cleaner abseiling on a rope with a bucket"></div>
  </section>

</main>
</body>
</html>
```